Business Card for Ferncliff Massage

I need a business card for my massage therapy & cannabis oil practice. I already have a logo,the "massage" got edited out of this file. I will send the original soon. I need these elements to be on the card:
web: FerncliffMassage.example
ph: 541/382-9147
email: Marla.Quintavelle@mailbox.example
Other slogans, statements to consider:
Science Geek, Massage Therapist, Neuromuscular Therapy, Cannabis Spa Treatments, Raindrop Therapy, Essential Oils
Target Market(s)
women between 20 & 65, people with enough $ to afford regular massage, people who recently had a motor vehicle accident, Halvora HMC insured
Industry/Entity Type
Massage Therapy
Contact Information for Business Card
I would like to see my bear logo featured; contact details, greens & blues preferred colors.

```html
<!DOCTYPE html>
<html lang="en">
<head>
<meta charset="utf-8">
<title>Ferncliff Massage — Business Card</title>
<link rel="stylesheet" href="https://fonts.googleapis.com/css2?family=Source+Sans+3:wght@400;600;700&display=swap">
<style>
  :root {
    --page-bg: #2b2b2b;
    --front-light: #f8d978;
    --front-mid: #f1b443;
    --front-dark: #d9862a;
    --back-light: #9c8778;
    --back-dark: #6f5e53;
    --brand-green: #2f8a3a;
    --ink-gray: #6b5f58;
    --paper-white: #ffffff;
    --card-radius: 17px;
  }
  html, body {
    margin: 0;
    padding: 0;
    width: 1200px;
    height: 987px;
    overflow: hidden;
    background: var(--page-bg);
    font-family: "Source Sans 3", "Helvetica Neue", Arial, sans-serif;
  }
  .canvas {
    position: relative;
    width: 1200px;
    height: 987px;
  }
  .card {
    position: absolute;
    left: 293px;
    width: 615px;
    height: 351px;
    border-radius: var(--card-radius);
    overflow: hidden;
  }
  .card--front {
    top: 130px;
    background: radial-gradient(ellipse at 45% 40%, var(--front-light) 0%, var(--front-mid) 55%, var(--front-dark) 100%);
  }
  .card--back {
    top: 506px;
    background: radial-gradient(ellipse at 45% 45%, var(--back-light) 0%, var(--back-dark) 100%);
  }
  .brand {
    position: absolute;
    left: 28px;
    top: 30px;
    display: flex;
    align-items: center;
    gap: 10px;
  }
  .brand__mark {
    width: 22px;
    height: 22px;
    border-radius: 50%;
    background: var(--brand-green);
  }
  .brand__name {
    font-size: 34px;
    font-weight: 400;
    color: var(--brand-green);
    letter-spacing: 0.2px;
  }
  .hand-motif {
    position: absolute;
    right: 0;
    top: 0;
    width: 320px;
    height: 351px;
    background: radial-gradient(ellipse at 75% 70%, rgba(255,255,255,0.85) 0%, rgba(255,255,255,0.35) 45%, rgba(255,255,255,0) 75%);
  }
  .holder {
    position: absolute;
    left: 28px;
    top: 196px;
  }
  .holder__name {
    margin: 0;
    font-size: 21px;
    font-weight: 700;
    color: var(--brand-green);
  }
  .holder__license {
    margin: 2px 0 0;
    font-size: 15px;
    font-weight: 600;
    color: var(--ink-gray);
  }
  .contact {
    position: absolute;
    left: 28px;
    top: 261px;
    margin: 0;
    padding: 0;
    list-style: none;
  }
  .contact__item {
    display: flex;
    align-items: center;
    gap: 8px;
    height: 23.5px;
    font-size: 16px;
    color: var(--ink-gray);
  }
  .contact__icon {
    width: 13px;
    height: 13px;
    fill: var(--brand-green);
    flex: none;
  }
  .back-brand {
    position: absolute;
    left: 40px;
    top: 150px;
    width: 230px;
    display: flex;
    align-items: center;
    justify-content: center;
    gap: 8px;
  }
  .back-brand__mark {
    width: 16px;
    height: 16px;
    border-radius: 50%;
    background: var(--paper-white);
  }
  .back-brand__name {
    font-size: 24px;
    font-weight: 400;
    color: var(--paper-white);
  }
  .divider {
    position: absolute;
    left: 274px;
    top: 105px;
    width: 1px;
    height: 134px;
    background: rgba(255,255,255,0.6);
  }
  .services {
    position: absolute;
    left: 302px;
    top: 112px;
    color: var(--paper-white);
  }
  .services__title {
    margin: 0 0 8px;
    font-size: 19px;
    font-weight: 700;
  }
  .services__list {
    margin: 0;
    padding-left: 16px;
  }
  .services__item {
    font-size: 16px;
    line-height: 24.5px;
  }
</style>
</head>
<body>
<main class="canvas">
  <section class="card card--front" aria-label="Business card front">
    <div class="hand-motif" role="img" aria-label="Large decorative open hand motif with spiral"></div>
    <div class="brand">
      <span class="brand__mark"></span>
      <span class="brand__name">Ferncliff Massage</span>
    </div>
    <div class="holder">
      <h1 class="holder__name">Marla Quintavelle, MPA</h1>
      <p class="holder__license">LMT#5186</p>
    </div>
    <ul class="contact">
      <li class="contact__item">
        <svg class="contact__icon" viewBox="0 0 24 24" aria-hidden="true"><path d="M6.6 10.8a15.1 15.1 0 0 0 6.6 6.6l2.2-2.2a1 1 0 0 1 1-.25 11.4 11.4 0 0 0 3.6.57 1 1 0 0 1 1 1V20a1 1 0 0 1-1 1A17 17 0 0 1 3 4a1 1 0 0 1 1-1h3.5a1 1 0 0 1 1 1c0 1.25.2 2.45.57 3.57a1 1 0 0 1-.25 1z"/></svg>
        541/382-9147
      </li>
      <li class="contact__item">
        <svg class="contact__icon" viewBox="0 0 24 24" aria-hidden="true"><path d="M2 5h20v14H2z M2 5l10 8 10-8" fill="none" stroke="#2f8a3a" stroke-width="0"/><path d="M2 5h20v2l-10 7L2 7zM2 9l10 7 10-7v10H2z"/></svg>
        Marla.Quintavelle@mailbox.example
      </li>
      <li class="contact__item">
        <svg class="contact__icon" viewBox="0 0 24 24" aria-hidden="true"><circle cx="12" cy="12" r="11"/><path d="M1 12h22M12 1c3 3 4.5 7 4.5 11S15 20 12 23c-3-3-4.5-7-4.5-11S9 4 12 1z" fill="none" stroke="#f4c35a" stroke-width="1.6"/></svg>
        FerncliffMassage.example
      </li>
    </ul>
  </section>

  <section class="card card--back" aria-label="Business card back">
    <div class="back-brand">
      <span class="back-brand__mark"></span>
      <span class="back-brand__name">Ferncliff Massage</span>
    </div>
    <div class="divider"></div>
    <div class="services">
      <h2 class="services__title">SERVICES</h2>
      <ul class="services__list">
        <li class="services__item">Neuromuscular Therapy</li>
        <li class="services__item">Cannabis Spa Treatments</li>
        <li class="services__item">Raindrop Therapy</li>
        <li class="services__item">Essential Oils</li>
      </ul>
    </div>
  </section>
</main>
</body>
</html>
```